789Gigtunes

We only need one indexpage mockup design.

a redesign for our current page which you can see on www.brightvenue.example

I have made a very good video here that explains:
http://www.vidplexa.example/watch?v=qTzRw8nLp2e

And this one which goes through the content: http://www.vidplexa.example/watch?v=hXdMu3fVbGj

We help people find bands, DJ and solomusicians for their events.
The goal is to make them create a free enquiry.
The company has been runing since 2005 and the simple, easy webpage has worked very good for us, so dont make it too fancy

Reason: Sorry. I have set a wrong deadline

Target Market(s)

People from northern Europe, between 29 and 55
PLanning the event of their lifetime - big wedding or big birthday.
Looking for great live musicians who can make their event great

Industry/Entity Type

It Company

Requirements
Must have
• Simplicity and great usability
Nice to have
• Watch the video:http://www.vidplexa.example/watch?v=hXdMu3fVbGj
Should not have
• - NO Fancy colours
- Should NOT only be focused on Young pepople, but also target the older
- Not too dark colours

```html
<!DOCTYPE html>
<html lang="en">
<head>
<meta charset="utf-8">
<title>789Gigtunes – Find bands, DJs and solo musicians</title>
<link rel="stylesheet" href="https://fonts.googleapis.com/css2?family=PT+Sans:wght@400;700&display=swap">
<style>
  :root {
    --stage-deep: #0a1630;
    --stage-blue: #2a63a8;
    --stage-glow: #7fc4ee;
    --page-white: #ffffff;
    --ink: #2b2b2b;
    --ink-soft: #3d3d3d;
    --orange: #f0622a;
    --orange-deep: #e1461c;
    --orange-light: #f7894a;
    --red-tab: #dd2630;
    --red-tab-dark: #b8141e;
    --box-line: #cfcfcf;
    --box-fill-top: #ffffff;
    --box-fill-bottom: #ececec;
    --badge-green: #3f9a2f;
    --strip-grey: #d9d9d9;
  }
  * { box-sizing: border-box; margin: 0; padding: 0; }
  html, body { width: 1200px; height: 900px; overflow: hidden; }
  body {
    font-family: "PT Sans", sans-serif;
    color: var(--ink);
    position: relative;
  }
  .stage-backdrop {
    position: absolute; inset: 0;
    background:
      radial-gradient(ellipse at 50% 40%, var(--stage-glow) 0%, transparent 45%),
      radial-gradient(ellipse at 95% 60%, #6fe08a 0%, transparent 20%),
      radial-gradient(ellipse at 5% 70%, #5fd0a0 0%, transparent 20%),
      linear-gradient(180deg, var(--stage-blue) 0%, #1b3f78 55%, var(--stage-deep) 100%);
  }
  .page {
    position: absolute; left: 108px; top: 35px;
    width: 985px; height: 809px;
    background: var(--page-white);
    border-radius: 8px;
    box-shadow: 0 0 0 2px rgba(0,0,0,0.35), 0 6px 24px rgba(0,0,0,0.5);
    overflow: hidden;
  }
  .brand {
    position: absolute; left: 58px; top: 56px;
    display: flex; align-items: center; gap: 16px;
  }
  .brand-dot { width: 44px; height: 44px; border-radius: 50%; background: var(--orange); }
  .brand-name { font-size: 28px; font-weight: 700; color: var(--ink); }

  .hero-art { position: absolute; left: 0; top: 0; width: 985px; height: 313px; }

  .main-nav {
    position: absolute; left: 599px; top: 97px;
    display: flex; gap: 6px;
  }
  .main-nav a {
    display: block; height: 41px; padding: 7px 11px 0;
    color: #fff; text-decoration: none; font-size: 18px;
    background: linear-gradient(180deg, var(--red-tab), var(--red-tab-dark));
    border-radius: 6px 6px 0 0;
    border: 1px solid #fff;
    border-bottom: none;
  }

  .hero-title {
    position: absolute; left: 0; top: 176px; width: 985px;
    text-align: center; color: #fff;
    font-size: 34px; font-weight: 700; line-height: 42px;
    text-shadow: 0 2px 4px rgba(0,0,0,0.45);
  }

  .music-picker {
    position: absolute; left: 0; top: 313px; width: 985px; height: 92px;
    background: linear-gradient(180deg, var(--orange-light), var(--orange) 45%, var(--orange-deep));
    border-top: 2px solid #fff;
  }
  .music-picker h2 {
    position: absolute; left: 21px; top: 30px;
    color: #fff; font-size: 21px; font-weight: 700;
  }
  .picker-option {
    position: absolute; top: 10px; width: 141px; height: 72px;
    border: 1px solid #3a1a0a; border-radius: 6px;
    background: linear-gradient(135deg, #f27a2c 0%, #c44612 55%, #2a1206 100%);
    color: rgba(255,255,255,0.5); font-size: 24px; font-weight: 400;
    padding: 19px 0 0 8px;
  }
  .picker-option.band { left: 454px; }
  .picker-option.dj   { left: 618px; }
  .picker-option.solo { left: 782px; }

  .feature {
    position: absolute; top: 427px; width: 290px; height: 190px;
    border: 1px solid var(--box-line); border-radius: 5px;
    background: linear-gradient(180deg, var(--box-fill-top), var(--box-fill-bottom));
  }
  .feature.satisfaction { left: 23px; }
  .feature.size-one { left: 340px; }
  .feature.size-two { left: 660px; }
  .feature h3 {
    position: absolute; left: 17px; top: 14px;
    font-size: 21px; font-weight: 700; color: var(--ink);
  }
  .feature p {
    position: absolute; left: 122px; top: 47px; width: 164px;
    font-size: 15px; line-height: 19.8px; color: var(--ink-soft);
    white-space: nowrap;
  }
  .rating-badge {
    position: absolute; left: 8px; top: 50px; width: 110px; height: 114px;
    background: linear-gradient(180deg, #58b043, var(--badge-green));
    border-radius: 3px;
  }
  .feature-mark {
    position: absolute; left: 18px; top: 70px; width: 80px; height: 80px;
    border-radius: 50%; background: #f7d6c4;
  }

  .press-note {
    position: absolute; left: 230px; top: 624px; width: 470px; height: 48px;
    background: linear-gradient(180deg, #f2f2f2, var(--strip-grey));
    border-radius: 4px; border: 1px solid #c4c4c4;
  }
  .press-badge {
    position: absolute; left: 6px; top: 6px; width: 144px; height: 34px;
    background: linear-gradient(180deg, #b9c9a8, #8aa377); border-radius: 2px;
  }
  .press-note p {
    position: absolute; left: 158px; top: 5px;
    font-size: 12.5px; line-height: 18px; color: var(--ink);
    white-space: nowrap;
  }

  .enquiries {
    position: absolute; left: 23px; top: 680px; width: 926px; height: 121px;
    border: 1px solid var(--box-line); border-radius: 5px;
    background: linear-gradient(180deg, var(--box-fill-top), var(--box-fill-bottom));
  }
  .enquiries h2 {
    position: absolute; left: 15px; top: 8px;
    font-size: 18px; font-weight: 700; color: var(--orange);
  }
  .enquiry-table {
    position: absolute; left: 263px; top: 15px;
    border-collapse: collapse;
  }
  .enquiry-table th {
    font-size: 16px; font-weight: 700; color: var(--ink);
    text-align: left; padding: 0 0 6px; height: 24px;
  }
  .enquiry-table td {
    font-size: 13px; line-height: 17px; color: var(--ink-soft); padding: 0;
  }
  .enquiry-table .col-type { width: 123px; }
  .enquiry-table .col-city { width: 118px; padding-left: 18px; }
  .enquiry-table .col-fest { width: 118px; }
  .enquiry-table .col-area { width: 102px; padding-left: 15px; }
  .enquiry-table .col-guests { width: 100px; padding-left: 9px; }
  .view-all {
    position: absolute; right: 34px; bottom: 10px;
    font-size: 13px; color: var(--orange); text-decoration: underline;
  }
</style>
</head>
<body>
  <div class="stage-backdrop" role="img" aria-label="Concert crowd under blue stage lights and laser beams"></div>

  <main class="page">
    <svg class="hero-art" viewBox="0 0 985 313" role="img" aria-label="Party venue with a lit stage and coloured lights">
      <defs>
        <linearGradient id="venueTone" x1="0" y1="0" x2="1" y2="1">
          <stop offset="0" stop-color="#7a2a5a"/>
          <stop offset="0.45" stop-color="#c44a6a"/>
          <stop offset="0.7" stop-color="#e88a3a"/>
          <stop offset="1" stop-color="#4a1a3a"/>
        </linearGradient>
        <linearGradient id="swoosh" x1="0" y1="0" x2="1" y2="0">
          <stop offset="0" stop-color="#e1461c"/>
          <stop offset="0.6" stop-color="#f26a2a"/>
          <stop offset="1" stop-color="#e1461c"/>
        </linearGradient>
      </defs>
      <path d="M0,205 C160,128 320,100 520,104 C720,108 860,140 985,112 L985,313 L0,313 Z" fill="url(#venueTone)"/>
      <path d="M0,205 C160,128 320,100 520,104 C720,108 860,140 985,112 L985,86 C860,120 720,96 520,92 C320,90 150,110 0,182 Z" fill="url(#swoosh)"/>
    </svg>

    <div class="brand">
      <span class="brand-dot"></span>
      <span class="brand-name">789gigtunes.example</span>
    </div>

    <nav class="main-nav">
      <a href="#">New artists</a>
      <a href="#">Find delete enquiry</a>
      <a href="#">About</a>
    </nav>

    <h1 class="hero-title">25000 bands, Djs and solomusicians are ready to send<br>you offers on next event</h1>

    <section class="music-picker">
      <h2>Which type of music are you looking for ?</h2>
      <a class="picker-option band" role="img" aria-label="Band performing on stage">Band</a>
      <a class="picker-option dj" role="img" aria-label="DJ at the decks">DJ</a>
      <a class="picker-option solo" role="img" aria-label="Solo guitarist">Solo</a>
    </section>

    <article class="feature satisfaction">
      <h3>Satification</h3>
      <div class="rating-badge" role="img" aria-label="Customer rating badge"></div>
      <p>Loream ipusum loream<br>ipusum loream ipusum<br>loream ipusum loream<br>ipusum loream ipusum<br>loream ipusum loream<br>loream ipusum loream</p>
    </article>

    <article class="feature size-one">
      <h3>Biggest in Denmark</h3>
      <div class="feature-mark"></div>
      <p>Loream ipusum loream<br>ipusum loream ipusum<br>loream ipusum loream<br>ipusum loream ipusum<br>loream ipusum loream<br>loream ipusum loream</p>
    </article>

    <article class="feature size-two">
      <h3>Biggest in Denmark</h3>
      <div class="feature-mark"></div>
      <p>Loream ipusum loream<br>ipusum loream ipusum<br>loream ipusum loream<br>ipusum loream ipusum<br>loream ipusum loream<br>loream ipusum loream</p>
    </article>

    <aside class="press-note">
      <div class="press-badge" role="img" aria-label="Radio programme feature"></div>
      <p>789gigtunes has been recommended on NordRadio's<br>Bargain Corner under our old name allforparty.example</p>
    </aside>

    <section class="enquiries">
      <h2>Newest enquiries</h2>
      <table class="enquiry-table">
        <thead>
          <tr>
            <th class="col-type">Music type</th>
            <th class="col-city">City</th>
            <th class="col-fest">Festtype</th>
            <th class="col-area">Area</th>
            <th class="col-guests">Guests</th>
          </tr>
        </thead>
        <tbody>
          <tr><td>Event #1111</td><td>Event #1111</td><td>Event #1111</td><td>Event #1111</td><td>Event #1111</td></tr>
          <tr><td>Event #1111</td><td>Event #1111</td><td>Event #1111</td><td>Event #1111</td><td>Event #1111</td></tr>
          <tr><td>Event #1111</td><td>Event #1111</td><td>Event #1111</td><td>Event #1111</td><td>Event #1111</td></tr>
          <tr><td>Event #1111</td><td>Event #1111</td><td>Event #1111</td><td>Event #1111</td><td>Event #1111</td></tr>
        </tbody>
      </table>
      <a class="view-all" href="#">view all</a>
    </section>
  </main>
</body>
</html>
```